見本のチラシがありますので、構成とレイアウトは流用していただき、ブラッシュアップしたデザインを期待します。

カラーパレットは以下です。

#F9F4EA
#FFFFFF
#444444
#666666
#F0E3CA
#DB887F
#E4BE7B
#83B2A6

ウェブサイトとロゴの仮デザインもお送りいたします。
チラシは統一感はそこまで必要ないですが、ご参考ください。

また画像は既存園のウェブサイトより流用していただければと思います。

https://kurumiya-hoiku.jp/
見本チラシとの差異をお送りいたします。

ロゴ

月額保育料
平日9:00〜16:00 週3日  0円
平日9:00〜18:00 週5日  10,000円

2021年3月開演予定

まかろん保育園 東戸塚
〒231-0917 神奈川県横浜市戸塚区柳瀬町718-6
MK「東戸塚駅」より徒歩13分

http://makahoiku.jp/lp

株式会社ルナメル
神奈川県横浜市神奈川区緑丘町8-7
横浜リバーテラスビル14階

ーーーーー

見本チラシに追加の要素です。

系列園「くるみや保育園」
https://kurumiya-hoiku.jp/

保育士募集は少し大きめにお願いします。
「詳細はお問い合わせください」「045-731-5184」「担当:森岡」のキーワードをお願いします。
A4
片面
黄・オレンジ系
AIデータに加えて、印刷所へ納品する入稿データまでお願いいたします。
13日中に提案していただいた案を優先いたします。
最終納品は14日の15時と考えております。
よろしくお願い申し上げます。

集まりが悪かった場合は17日まで延期いたします。
http://makahoiku.jp/lp

https://makahoiku.jp/lp

URLがSSLになっておりませんでした。
よろしくお願い申し上げます。

要件を最も満たしていました。デザインのクオリティも素晴らしかったです。

コンペに参加していただきまして、ありがとうございます。
またよろしくお願い申し上げます。

```html
<!DOCTYPE html>
<html lang="ja">
<head>
<meta charset="utf-8">
<title>まかろん保育園 東戸塚 園児募集</title>
<link rel="stylesheet" href="https://fonts.googleapis.com/css2?family=M+PLUS+Rounded+1c:wght@400;700;800&display=swap">
<style>
:root{
  --cream:#F9F4EA;
  --white:#FFFFFF;
  --ink:#444444;
  --ink-soft:#666666;
  --beige:#F0E3CA;
  --pink:#DB887F;
  --gold:#E4BE7B;
  --mint:#83B2A6;
  --yellow:#F7D86E;
  --yellow-deep:#F2C84B;
}
*{margin:0;padding:0;box-sizing:border-box}
html,body{width:849px;height:1200px;overflow:hidden;background:var(--white)}
body{font-family:"M PLUS Rounded 1c",sans-serif;color:var(--ink)}
.flyer{position:relative;width:849px;height:1200px;overflow:hidden;background:var(--yellow)}
.abs{position:absolute}
.stripes{left:0;top:0;width:849px;height:770px;background:linear-gradient(180deg,var(--yellow) 0%,#F9DE85 100%)}
.photo{border-radius:14px;background:linear-gradient(135deg,#F3D9BE,#D9B99A 60%,#C9A98C)}
.photo.round{border-radius:50%}
.kicker{left:0;width:849px;top:28px;text-align:center;font-size:27px;font-weight:800;color:var(--pink);letter-spacing:2px}
.headline{left:60px;top:68px;display:flex;align-items:center;gap:6px}
.headline .bubble{width:112px;height:112px;border-radius:50%;background:var(--white);display:flex;align-items:center;justify-content:center;font-size:86px;font-weight:800;color:var(--pink);border:5px solid var(--pink)}
.headline .word{font-size:104px;font-weight:800;color:var(--mint);line-height:1;margin-left:8px;letter-spacing:2px}
.headline .bang{font-size:96px;font-weight:800;color:var(--pink);line-height:1}
.fees{left:55px;top:200px;width:740px;height:134px;background:var(--white);border-radius:16px;border:3px solid var(--pink)}
.fees-title{position:absolute;left:50%;top:-16px;transform:translateX(-50%);background:var(--pink);color:var(--white);font-weight:800;font-size:19px;padding:4px 26px;border-radius:20px;white-space:nowrap}
.fees-title small{font-size:13px;font-weight:700}
.fee-col{position:absolute;top:26px}
.fee-col.general{left:22px;width:360px}
.fee-col.staff{left:400px;width:320px;border-left:2px dashed var(--gold);padding-left:18px}
.fee-label{font-size:21px;font-weight:800;color:var(--pink);margin-bottom:8px}
.fee-label small{font-size:12px;color:var(--ink-soft)}
.fee-row{display:flex;align-items:center;justify-content:space-between;background:var(--cream);border-radius:8px;padding:5px 10px;margin-bottom:6px;font-size:15px;font-weight:700}
.fee-row b{color:var(--pink);font-size:20px;font-weight:800}
.fee-note{left:60px;top:340px;width:560px;font-size:10px;line-height:1.5;color:var(--ink-soft)}
.opening{left:22px;top:388px;background:var(--pink);color:var(--white);font-size:26px;font-weight:800;padding:6px 22px 6px 18px;clip-path:polygon(0 0,100% 0,94% 50%,100% 100%,0 100%)}
.school{left:22px;top:445px;width:410px;background:var(--white);border-radius:12px;padding:12px 16px}
.school h2{font-size:24px;font-weight:800;color:var(--ink)}
.school p{font-size:12.5px;line-height:1.6;color:var(--ink-soft)}
.map{left:200px;top:540px;width:232px;height:168px;border-radius:10px;background:linear-gradient(135deg,#FBF7EF,#EDE3CF);border:2px solid var(--white)}
.zero-class{left:640px;top:330px;width:190px;height:190px;border-radius:50%;background:var(--white);border:5px dashed var(--pink);display:flex;flex-direction:column;align-items:center;justify-content:center;text-align:center;font-weight:800;color:var(--pink)}
.zero-class .big{font-size:34px;line-height:1.1}
.zero-class .small{font-size:20px;color:var(--ink)}
.visit{left:455px;top:560px;width:78px;height:78px;border-radius:50%;background:var(--mint);color:var(--white);font-size:15px;font-weight:800;display:flex;align-items:center;justify-content:center;text-align:center;line-height:1.2}
.homey{left:635px;top:560px;width:96px;height:96px;border-radius:50%;background:var(--white);border:3px solid var(--gold);font-size:12px;font-weight:700;color:var(--ink);display:flex;align-items:center;justify-content:center;text-align:center;line-height:1.35}
.lower{left:0;top:770px;width:849px;height:430px;background:var(--white)}
.logo-mark{left:60px;top:790px;width:130px;display:flex;flex-direction:column;align-items:center;gap:6px}
.logo-mark .dot{width:58px;height:58px;border-radius:50%;background:var(--gold)}
.logo-mark span{font-size:15px;font-weight:700;color:var(--pink)}
.school-title{left:220px;top:792px}
.school-title small{display:block;font-size:15px;font-weight:700;color:var(--ink-soft)}
.school-title strong{font-size:46px;font-weight:800;color:var(--pink);letter-spacing:1px}
.guide{left:210px;top:880px;width:600px;background:var(--pink);color:var(--white);font-size:19px;font-weight:800;text-align:center;padding:5px 0;border-radius:18px}
.url-band{left:40px;top:922px;width:770px;background:var(--gold);border-radius:10px;text-align:center;padding:6px 0;font-size:34px;font-weight:800;color:var(--white);letter-spacing:1px}
.company{left:24px;top:1000px;width:250px;font-size:11.5px;line-height:1.6;color:var(--ink-soft)}
.company h3{font-size:22px;font-weight:800;color:var(--ink);margin-bottom:4px}
.recruit{left:278px;top:990px;width:300px;text-align:center;border-left:2px solid var(--beige);border-right:2px solid var(--beige);height:190px;padding-top:8px}
.recruit .title{font-size:44px;font-weight:800;color:var(--mint);line-height:1.1}
.recruit .title span{font-size:26px;color:var(--pink)}
.recruit .detail{font-size:14px;font-weight:700;color:var(--ink-soft);margin:8px 0 4px}
.recruit .tel{display:flex;align-items:center;justify-content:center;gap:6px;font-size:30px;font-weight:800;color:var(--pink)}
.recruit .person{font-size:15px;font-weight:700;color:var(--ink)}
.affiliate{left:596px;top:1000px;width:235px}
.affiliate .tag{display:inline-block;background:var(--mint);color:var(--white);font-size:13px;font-weight:800;padding:2px 12px;border-radius:12px}
.affiliate .name{display:flex;align-items:center;gap:8px;margin:12px 0 8px;font-size:24px;font-weight:800;color:var(--ink)}
.affiliate .name i{width:26px;height:26px;border-radius:50%;background:var(--gold);display:block}
.affiliate .url{font-size:14px;font-weight:700;color:var(--ink-soft)}
.footer-bar{left:0;top:1186px;width:849px;height:14px;background:var(--yellow-deep)}
</style>
</head>
<body>
<main class="flyer">
  <div class="abs stripes"></div>
  <div class="abs photo" style="left:650px;top:0;width:199px;height:150px;border-radius:0 0 0 30px" role="img" aria-label="園で遊ぶ子どもの写真"></div>

  <p class="abs kicker">企業主導型 小規模保育園</p>
  <h1 class="abs headline">
    <span class="bubble">園</span><span class="bubble">児</span>
    <span class="word">募集</span><span class="bang">!!</span>
  </h1>

  <section class="abs fees">
    <div class="fees-title">月額保育料 <small>（給食費・教材費を含む）</small></div>
    <div class="fee-col general">
      <p class="fee-label">一般利用 <small>（一般）</small></p>
      <div class="fee-row"><span>平日9時〜16時 週3日</span><b>0円</b></div>
      <div class="fee-row"><span>平日9時〜18時 週5日</span><b>10,000円</b></div>
    </div>
    <div class="fee-col staff">
      <p class="fee-label">当社スタッフとして<br>勤務している場合 <small>（一般）</small></p>
      <div class="fee-row"><span>平日9時〜18時 週5日</span><b>0円</b></div>
    </div>
  </section>
  <p class="abs fee-note">※保育料は市の基準に準じます。詳しくは園までお問い合わせください。<br>※利用日数や時間については、ご相談に応じます。</p>

  <div class="abs opening">2021年3月開園予定</div>
  <section class="abs school">
    <h2>まかろん保育園 東戸塚</h2>
    <p>〒231-0917 神奈川県横浜市戸塚区柳瀬町718-6<br>MK「東戸塚駅」より徒歩13分</p>
  </section>
  <div class="abs photo" style="left:22px;top:540px;width:168px;height:168px" role="img" aria-label="保護者と子どもの写真"></div>
  <div class="abs map" role="img" aria-label="園周辺の案内地図"></div>
  <div class="abs photo" style="left:22px;top:718px;width:200px;height:44px;border-radius:10px 10px 0 0" role="img" aria-label="子どもたちの写真"></div>

  <div class="abs zero-class"><span class="big">0歳クラス</span><span class="small">園児募集中!</span></div>
  <div class="abs photo" style="left:455px;top:405px;width:170px;height:140px" role="img" aria-label="保育室で遊ぶ子どもたちの写真"></div>
  <div class="abs photo" style="left:545px;top:560px;width:80px;height:110px" role="img" aria-label="子どもの写真"></div>
  <div class="abs visit">見学<br>受付中</div>
  <div class="abs homey">定員19名の<br>アットホーム<br>保育園です</div>
  <div class="abs photo" style="left:742px;top:540px;width:92px;height:160px;background:linear-gradient(135deg,#FBEFD8,#F0E3CA)" role="img" aria-label="Welcomeの看板イラスト"></div>
  <div class="abs photo" style="left:455px;top:680px;width:280px;height:82px;border-radius:10px 10px 0 0" role="img" aria-label="園庭で遊ぶ子どもたちの写真"></div>

  <div class="abs lower"></div>
  <div class="abs logo-mark"><i class="dot"></i><span>まかろん保育園</span></div>
  <div class="abs school-title"><small>企業主導型保育園</small><strong>まかろん保育園 東戸塚</strong></div>
  <p class="abs guide">入園希望の方は下記ホームページをご確認ください!</p>
  <p class="abs url-band">https://makahoiku.jp/lp</p>

  <section class="abs company">
    <h3>株式会社ルナメル</h3>
    <p>神奈川県横浜市神奈川区緑丘町8-7<br>横浜リバーテラスビル14階</p>
  </section>
  <section class="abs recruit">
    <p class="title">保育士<span>募集中</span></p>
    <p class="detail">詳細はお問い合わせください</p>
    <p class="tel">
      <svg width="28" height="28" viewBox="0 0 24 24" aria-hidden="true"><path fill="#DB887F" d="M6.6 10.8a15.1 15.1 0 0 0 6.6 6.6l2.2-2.2c.3-.3.7-.4 1-.2 1.1.4 2.3.6 3.6.6.6 0 1 .4 1 1V20c0 .6-.4 1-1 1A17 17 0 0 1 3 4c0-.6.4-1 1-1h3.5c.6 0 1 .4 1 1 0 1.3.2 2.5.6 3.6.1.3 0 .7-.2 1z"/></svg>
      045-731-5184
    </p>
    <p class="person">担当:森岡</p>
  </section>
  <section class="abs affiliate">
    <span class="tag">系列園</span>
    <p class="name"><i></i>くるみや保育園</p>
    <p class="url">https://kurumiya-hoiku.jp/</p>
  </section>
  <div class="abs footer-bar"></div>
</main>
</body>
</html>
```